Cedar Lantern (short term rental)

This website will be for a short term rental (roost k&k) located in a small quant town called Medicine Park and at the entrance of the Harrow Pines Refuge. I am currently in a logo contest and will have the logo soon to use on the website My goal for the website is to highlight the home and area with photographs, text, and possibly a rotating video/slide show of the local area. I will soon have a professional photographer at the home and will upload my own photos to the site with your instructions. I want a booking option for customers to use vs hosting sites like QELT and roost k&K. . I would like cedarlantern.org ( or .com—-appreciate your guidance here) for the web address. And I want it to appear on search engines with words like, medicine park, medicine park rental, rental near Wichita mountains, etc. I hope you can help me. Thanks!

Target Market(s)

Outdoor enthusiasts (bikers, hikers, lakers, etc) festival attendees, hippies.

Industry/Entity Type

Short term rental

Coding

Coded - Design and coding required

Number of Pages Required

1 page

Font styles to use
Serif

Colors
00AB8E
00BBA5
67D7C9
C6EFE9
E9F9F6

Requirements
Must have
• Booking calendar, reviews section, contact us section, brief over view of the area, place to upload my photos

```html
<!DOCTYPE html>
<html lang="en">
<head>
<meta charset="utf-8">
<title>Cedar Lantern — Short Term Rental</title>
<link rel="stylesheet" href="https://fonts.googleapis.com/css2?family=Lato:ital,wght@0,400;0,700;0,900;1,400&display=swap">
<style>
:root{
  --green:#19a98b;
  --green-dark:#12977b;
  --teal:#00bba5;
  --teal-light:#67d7c9;
  --mint:#c6efe9;
  --mint-pale:#e9f9f6;
  --ink:#1c1c1c;
  --text:#444;
  --muted:#c7c7c7;
  --dark:#1f1f1f;
  --white:#fff;
}
*{box-sizing:border-box;margin:0;padding:0}
html,body{width:1200px;height:4370px;overflow:hidden}
body{position:relative;font-family:"Lato",sans-serif;color:var(--text);background:var(--white)}
.abs{position:absolute}
.btn{position:absolute;display:flex;align-items:center;justify-content:center;background:var(--green);color:var(--white);border-radius:22px;font-size:14px;font-weight:700;text-transform:uppercase}
.heading{position:absolute;font-weight:900;color:var(--ink);text-transform:uppercase;line-height:1;padding-left:20px;border-left:4px solid var(--green)}
.fill{position:absolute;display:block}

/* header */
.site-header{position:absolute;left:0;top:0;width:1200px;height:97px;background:var(--white)}
.brand{position:absolute;left:143px;top:27px;font-size:35px;font-weight:900;color:var(--ink);letter-spacing:-.5px}
.nav{position:absolute;top:38px;display:flex;font-size:13px;font-weight:700;color:var(--ink)}
.nav a{position:absolute;white-space:nowrap}
.nav .active{border-left:3px solid var(--green);padding-left:7px}

/* hero */
.hero-panel{position:absolute;left:144px;top:219px;width:438px;height:319px;background:rgba(24,24,24,.88)}
.hero-title{position:absolute;left:196px;top:253px;font-size:59px;font-weight:900;color:var(--white);line-height:62px;text-transform:uppercase;border-left:3px solid var(--green);padding-left:14px;margin-left:-17px}
.dot{position:absolute;left:1129px;width:16px;height:16px;border-radius:50%;background:var(--white)}

/* about */
.about-frame{position:absolute;left:590px;top:638px;width:466px;height:501px;background:var(--green)}
.about-frame::after{content:"";position:absolute;left:0;top:22px;width:444px;height:479px;background:var(--white)}
.about-text{position:absolute;left:144px;top:840px;width:403px;font-size:14px;line-height:25.6px;text-align:justify}

/* booking */
.booking-intro{position:absolute;left:0;top:1404px;width:1200px;text-align:center;color:var(--white);font-size:14.5px;line-height:26px}
.cal-card{position:absolute;left:594px;top:1522px;width:606px;height:445px;background:var(--white);box-shadow:0 4px 14px rgba(0,0,0,.18)}
.cal-bar{position:absolute;left:711px;top:1522px;width:370px;height:51px;background:#1e1e1e;box-shadow:0 4px 10px rgba(0,0,0,.3);color:var(--white);font-size:23px;font-weight:700;display:flex;align-items:center;justify-content:center}
.cal-arrow{position:absolute;top:9px;width:34px;height:34px;border-radius:50%;background:var(--white)}
.cal-cell{position:absolute;width:60px;margin-left:-30px;text-align:center;font-size:17px;color:#333}
.cal-head{font-weight:700;font-size:17px;color:#222}
.cal-off{color:var(--muted)}
.cal-sel{color:var(--white)}
.cal-caption{position:absolute;left:0;top:1833px;width:594px;height:134px;background:rgba(20,20,20,.8);text-align:center;color:var(--white)}
.cal-caption h4{margin-top:36px;font-size:14.5px;font-weight:700;color:var(--green)}
.cal-caption p{margin-top:18px;font-size:12.5px;line-height:21px}

/* gallery */
.round-arrow{position:absolute;width:42px;height:42px;border-radius:50%;border:2px solid #555;background:var(--white)}
.card{position:absolute;width:293px;height:361px;border:1px solid #ddd;background:var(--white)}
.card .photo{position:absolute;left:0;top:0;width:291px;height:194px}
.card h3{position:absolute;left:17px;top:216px;font-size:14px;font-weight:700;color:var(--green);text-transform:uppercase}
.card p{position:absolute;left:17px;top:243px;width:257px;font-size:12.5px;line-height:22.5px;text-align:justify}
.card .book{position:absolute;left:17px;top:322px;font-size:13px;font-weight:900;color:var(--ink);text-decoration:underline}
.card .list{position:absolute;top:321px;font-size:13px;font-weight:700;color:#7a86b3}

/* reviews */
.review-quote{position:absolute;left:0;top:3245px;width:1200px;text-align:center;color:var(--white);font-size:21.5px;font-style:italic;line-height:34px}
.review-name{position:absolute;left:0;top:3367px;width:1200px;text-align:center;color:var(--white);font-size:21px}
.review-name b{font-weight:900}
.wh-arrow{position:absolute;top:3448px;width:42px;height:42px;border-radius:50%;border:2px solid var(--white)}

/* contact */
.field{position:absolute;height:51px;border:1px solid #bbb;background:var(--white);font-size:15px;color:#444;padding:16px 20px}

/* footer */
.site-footer{position:absolute;left:0;top:4183px;width:1200px;height:187px;background:var(--dark);color:var(--white)}
.foot-link{position:absolute;top:43px;font-size:13px;font-weight:700}
.social{position:absolute;top:76px;width:40px;height:40px;border:2px solid var(--white);border-radius:50%}
.social::after{content:"";position:absolute;left:13px;top:13px;width:10px;height:10px;background:var(--white);border-radius:2px}
</style>
</head>
<body>

<header class="site-header">
  <div class="brand">CEDAR LANTERN</div>
  <nav class="nav">
    <a class="active" style="left:564px">HOME</a>
    <a style="left:650px">ABOUT</a>
    <a style="left:731px">REVIEWS</a>
    <a style="left:825px">CONTACT US</a>
  </nav>
  <a class="btn" style="left:937px;top:25px;width:117px;height:40px;font-weight:400">Book Now</a>
</header>

<section class="hero">
  <svg class="fill" style="left:0;top:97px" width="1200" height="563" role="img" aria-label="Photo of old stone ruins on a rocky hillside under a cloudy blue sky">
    <defs><linearGradient id="heroG" x1="0" y1="0" x2="0" y2="1">
      <stop offset="0" stop-color="#3a5a8c"/><stop offset=".35" stop-color="#8a9ab0"/>
      <stop offset=".6" stop-color="#7b6448"/><stop offset="1" stop-color="#6b4a34"/></linearGradient></defs>
    <rect width="1200" height="563" fill="url(#heroG)"/>
  </svg>
  <div class="hero-panel"></div>
  <h1 class="hero-title">Harrow<br>Pines<br>Refuge</h1>
  <a class="btn" style="left:197px;top:460px;width:119px;height:40px;font-weight:400">Book Now</a>
  <span class="dot" style="top:338px"></span>
  <span class="dot" style="top:370px;background:var(--green)"></span>
  <span class="dot" style="top:403px"></span>
</section>

<section class="about">
  <div class="about-frame"></div>
  <svg class="fill" style="left:582px;top:675px" width="435" height="472" role="img" aria-label="Photo of a small chapel tower with snowy mountains behind">
    <defs><linearGradient id="aboutG" x1="0" y1="0" x2="1" y2="1">
      <stop offset="0" stop-color="#4f6e96"/><stop offset=".45" stop-color="#c9ccd0"/>
      <stop offset=".7" stop-color="#e6e6e4"/><stop offset="1" stop-color="#5a5046"/></linearGradient></defs>
    <rect width="435" height="472" fill="url(#aboutG)"/>
  </svg>
  <h2 class="heading" style="left:144px;top:762px;font-size:57px">About Us</h2>
  <p class="about-text">Lorem ipsum dolor sit amet, consectetur adipiscing elit, sed do eiusmod tempor incididunt ut labore et dolore magna psum suspendisse ultrices gravida. Risus commodo viverra maecenas accumsan lacus vel facilisis. Lorem ipsum dolor sit amet, consectetur adipiscind do eiusmod tempor incididunt ut labore et dolore magna psum suspendisse ultrices gravida. Risus commodo viverraas accumsan lacus vel facilisis. Lorem ipsum dolor sit amet, consectetur adipiscing elit, sed do eius-mod tempor incididunt ut labore et dolore magna</p>
  <a class="btn" style="left:144px;top:1098px;width:119px;height:39px;font-weight:400">Read More</a>
</section>

<section class="booking">
  <svg class="fill" style="left:0;top:1240px" width="1200" height="282">
    <path d="M0 75 Q600 -60 1200 75 V282 H0Z" fill="var(--green)"/>
  </svg>
  <h2 class="heading" style="left:292px;top:1333px;font-size:57px;color:var(--white);border-color:var(--white)">Booking Calendar</h2>
  <p class="booking-intro">Lorem ipsum dolor sit amet, consectetur adipiscing elit, sed do eiusmod tempor incididunt ut labore et dolore magna aliqua.<br>Quis ipsum suspendisse ultrices gravida. Risus commodo viverra maecenas accumsan lacus vel facilisis.</p>

  <svg class="fill" style="left:0;top:1522px" width="594" height="445" role="img" aria-label="Photo of a mountain lodge in a green meadow below jagged peaks">
    <defs><linearGradient id="calG" x1="0" y1="0" x2="0" y2="1">
      <stop offset="0" stop-color="#b8c2c8"/><stop offset=".35" stop-color="#7c7e7c"/>
      <stop offset=".6" stop-color="#5e7a3c"/><stop offset="1" stop-color="#4f8a2c"/></linearGradient></defs>
    <rect width="594" height="445" fill="url(#calG)"/>
  </svg>
  <div class="cal-caption">
    <h4>ALIQUIP EX EA COMMODO CONSEQUA</h4>
    <p>Lorem ipsum dolor sit amet, consectetur adipiscing elit, sed<br>do eiusmod tempor incididunt ut labore et dolore</p>
  </div>

  <div class="cal-card"></div>
  <div class="cal-bar">SEPTEMBER 2022
    <span class="cal-arrow" style="left:19px"><svg width="34" height="34"><path d="M25 17H10M15 12l-5 5 5 5" stroke="#1e1e1e" stroke-width="2" fill="none"/></svg></span>
    <span class="cal-arrow" style="right:19px"><svg width="34" height="34"><path d="M9 17h15M19 12l5 5-5 5" stroke="#1e1e1e" stroke-width="2" fill="none"/></svg></span>
  </div>
  <div class="calendar">
    <span class="cal-cell cal-head" style="left:677px;top:1633px">MO</span>
    <span class="cal-cell cal-head" style="left:743px;top:1633px">TUE</span>
    <span class="cal-cell cal-head" style="left:823px;top:1633px">WED</span>
    <span class="cal-cell cal-head" style="left:894px;top:1633px">THU</span>
    <span class="cal-cell cal-head" style="left:967px;top:1633px">FRI</span>
    <span class="cal-cell cal-head" style="left:1040px;top:1633px">SAT</span>
    <span class="cal-cell cal-head" style="left:1113px;top:1633px">SUN</span>

    <span class="cal-cell cal-off" style="left:677px;top:1688px">29</span>
    <span class="cal-cell cal-off" style="left:743px;top:1688px">30</span>
    <span class="cal-cell cal-off" style="left:823px;top:1688px">31</span>
    <span class="cal-cell" style="left:894px;top:1688px">1</span>
    <span class="cal-cell" style="left:967px;top:1688px">2</span>
    <span class="cal-cell" style="left:1040px;top:1688px">3</span>
    <span class="cal-cell" style="left:1113px;top:1688px">4</span>

    <span class="cal-cell" style="left:677px;top:1741px">5</span>
    <svg class="fill" style="left:723px;top:1731px" width="40" height="40"><circle cx="20" cy="20" r="20" fill="var(--green)"/></svg>
    <span class="cal-cell cal-sel" style="left:743px;top:1741px">6</span>
    <span class="cal-cell" style="left:823px;top:1741px">7</span>
    <span class="cal-cell" style="left:894px;top:1741px">8</span>
    <span class="cal-cell" style="left:967px;top:1741px">9</span>
    <span class="cal-cell" style="left:1040px;top:1741px">10</span>
    <span class="cal-cell" style="left:1113px;top:1741px">11</span>

    <span class="cal-cell" style="left:677px;top:1794px">12</span>
    <span class="cal-cell" style="left:743px;top:1794px">13</span>
    <span class="cal-cell" style="left:823px;top:1794px">14</span>
    <span class="cal-cell" style="left:894px;top:1794px">15</span>
    <span class="cal-cell" style="left:967px;top:1794px">16</span>
    <span class="cal-cell" style="left:1040px;top:1794px">17</span>
    <span class="cal-cell" style="left:1113px;top:1794px">18</span>

    <span class="cal-cell" style="left:677px;top:1846px">19</span>
    <span class="cal-cell" style="left:743px;top:1846px">20</span>
    <span class="cal-cell" style="left:823px;top:1846px">21</span>
    <span class="cal-cell" style="left:894px;top:1846px">22</span>
    <span class="cal-cell" style="left:967px;top:1846px">23</span>
    <span class="cal-cell" style="left:1040px;top:1846px">24</span>
    <span class="cal-cell" style="left:1113px;top:1846px">25</span>

    <span class="cal-cell" style="left:677px;top:1899px">26</span>
    <span class="cal-cell" style="left:743px;top:1899px">27</span>
    <span class="cal-cell" style="left:823px;top:1899px">28</span>
    <span class="cal-cell" style="left:894px;top:1899px">29</span>
    <span class="cal-cell" style="left:967px;top:1899px">30</span>
    <span class="cal-cell cal-off" style="left:1040px;top:1899px">1</span>
    <span class="cal-cell cal-off" style="left:1113px;top:1899px">2</span>
  </div>
</section>

<section class="gallery">
  <h2 class="heading" style="left:144px;top:2092px;font-size:57px">Project Gallery</h2>
  <span class="round-arrow" style="left:963px;top:2097px"><svg width="38" height="38"><path d="M22 11l-8 8 8 8" stroke="#333" stroke-width="2.2" fill="none"/></svg></span>
  <span class="round-arrow" style="left:1011px;top:2097px"><svg width="38" height="38"><path d="M16 11l8 8-8 8" stroke="#333" stroke-width="2.2" fill="none"/></svg></span>

  <svg width="0" height="0" style="position:absolute"><defs>
    <linearGradient id="g1" x1="0" y1="0" x2="0" y2="1"><stop offset="0" stop-color="#6f9ad0"/><stop offset=".5" stop-color="#5b8a45"/><stop offset="1" stop-color="#6b5a45"/></linearGradient>
    <linearGradient id="g2" x1="0" y1="0" x2="0" y2="1"><stop offset="0" stop-color="#8fb0d6"/><stop offset=".45" stop-color="#7d8f4a"/><stop offset="1" stop-color="#4e7078"/></linearGradient>
    <linearGradient id="g3" x1="0" y1="0" x2="0" y2="1"><stop offset="0" stop-color="#8da6c6"/><stop offset=".45" stop-color="#5f6c55"/><stop offset="1" stop-color="#6b8a3b"/></linearGradient>
    <linearGradient id="g4" x1="0" y1="0" x2="0" y2="1"><stop offset="0" stop-color="#a9b8c8"/><stop offset=".45" stop-color="#6f7068"/><stop offset="1" stop-color="#5f5a2e"/></linearGradient>
    <linearGradient id="g5" x1="0" y1="0" x2="0" y2="1"><stop offset="0" stop-color="#4a78c2"/><stop offset=".5" stop-color="#4e7a30"/><stop offset="1" stop-color="#2f5a5c"/></linearGradient>
    <linearGradient id="g6" x1="0" y1="0" x2="0" y2="1"><stop offset="0" stop-color="#e08a3a"/><stop offset=".45" stop-color="#8a5a3a"/><stop offset="1" stop-color="#3e3a36"/></linearGradient>
  </defs></svg>

  <article class="card" style="left:144px;top:2201px">
    <svg class="photo" role="img" aria-label="Photo of a lodge in a green mountain valley"><rect width="291" height="194" fill="url(#g1)"/></svg>
    <h3>Consectetur adipiscing</h3>
    <p>Lorem ipsum dolor sit amet, consectetur adipiscing elit, sed do eiusmod tempor incididunt ut labore et dolore</p>
    <a class="book">BOOK NOW</a><span class="list" style="left:166px">QELT</span><span class="list" style="left:214px;color:#d9536b">roost k&amp;k</span>
  </article>
  <article class="card" style="left:453px;top:2201px">
    <svg class="photo" role="img" aria-label="Photo of a mountain lake reflecting green hills"><rect width="291" height="194" fill="url(#g2)"/></svg>
    <h3>Consectetur adipiscing</h3>
    <p>Lorem ipsum dolor sit amet, consectetur adipiscing elit, sed do eiusmod tempor incididunt ut labore et dolore</p>
    <a class="book">BOOK NOW</a><span class="list" style="left:166px">QELT</span><span class="list" style="left:214px;color:#d9536b">roost k&amp;k</span>
  </article>
  <article class="card" style="left:762px;top:2201px">
    <svg class="photo" role="img" aria-label="Photo of wooden chalets along a mountain road"><rect width="291" height="194" fill="url(#g3)"/></svg>
    <h3>Consectetur adipiscing</h3>
    <p>Lorem ipsum dolor sit amet, consectetur adipiscing elit, sed do eiusmod tempor incididunt ut labore et dolore</p>
    <a class="book">BOOK NOW</a><span class="list" style="left:166px">QELT</span><span class="list" style="left:214px;color:#d9536b">roost k&amp;k</span>
  </article>
  <article class="card" style="left:144px;top:2576px">
    <svg class="photo" role="img" aria-label="Photo of a cabin by a pond under rocky peaks"><rect width="291" height="194" fill="url(#g4)"/></svg>
    <h3>Consectetur adipiscing</h3>
    <p>Lorem ipsum dolor sit amet, consectetur adipiscing elit, sed do eiusmod tempor incididunt ut labore et dolore</p>
    <a class="book">BOOK NOW</a><span class="list" style="left:166px">QELT</span><span class="list" style="left:214px;color:#d9536b">roost k&amp;k</span>
  </article>
  <article class="card" style="left:453px;top:2576px">
    <svg class="photo" role="img" aria-label="Photo of a village beside a lake in green hills"><rect width="291" height="194" fill="url(#g5)"/></svg>
    <h3>Consectetur adipiscing</h3>
    <p>Lorem ipsum dolor sit amet, consectetur adipiscing elit, sed do eiusmod tempor incididunt ut labore et dolore</p>
    <a class="book">BOOK NOW</a><span class="list" style="left:166px">QELT</span><span class="list" style="left:214px;color:#d9536b">roost k&amp;k</span>
  </article>
  <article class="card" style="left:762px;top:2576px">
    <svg class="photo" role="img" aria-label="Photo of a hilltop town at sunset"><rect width="291" height="194" fill="url(#g6)"/></svg>
    <h3>Consectetur adipiscing</h3>
    <p>Lorem ipsum dolor sit amet, consectetur adipiscing elit, sed do eiusmod tempor incididunt ut labore et dolore</p>
    <a class="book">BOOK NOW</a><span class="list" style="left:166px">QELT</span><span class="list" style="left:214px;color:#d9536b">roost k&amp;k</span>
  </article>
</section>

<section class="reviews">
  <svg class="fill" style="left:0;top:3020px" width="1200" height="560" role="img" aria-label="Photo of green hills and a lakeside hotel under a teal overlay">
    <defs><linearGradient id="revG" x1="0" y1="0" x2="0" y2="1">
      <stop offset="0" stop-color="#33d2bd"/><stop offset=".5" stop-color="#1fb79b"/><stop offset="1" stop-color="#2e9a7a"/></linearGradient></defs>
    <path d="M0 85 Q600 -75 1200 85 V476 Q600 620 0 476Z" fill="url(#revG)"/>
  </svg>
  <h2 class="heading" style="left:297px;top:3146px;font-size:57px;color:var(--white);border-color:var(--white)">Customer Reviews</h2>
  <p class="review-quote">“Lorem ipsum dolor sit amet, consectetur adipiscing elit, sed do eiusmod tempor<br>incididunt ut labore et dolore magna aliquauis ipsum suspendisse ultrices<br>gravidisus commodo viverra maecenas accumsan lacus vse ultrices”</p>
  <p class="review-name"><b>JOHN DOE</b>,<i>Customer</i>
    <svg width="130" height="24" style="vertical-align:-3px;margin-left:12px"><g fill="#f5b82e">
      <path id="star" d="M12 1l3.4 7 7.6 1-5.5 5.3 1.3 7.6L12 18.3 5.2 21.9l1.3-7.6L1 9l7.6-1z"/>
      <use href="#star" x="26"/><use href="#star" x="52"/><use href="#star" x="78"/><use href="#star" x="104"/></g></svg>
  </p>
  <span class="wh-arrow" style="left:554px"><svg width="38" height="38"><path d="M22 11l-8 8 8 8" stroke="#fff" stroke-width="2.2" fill="none"/></svg></span>
  <span class="wh-arrow" style="left:602px"><svg width="38" height="38"><path d="M16 11l8 8-8 8" stroke="#fff" stroke-width="2.2" fill="none"/></svg></span>
</section>

<section class="contact">
  <svg class="fill" style="left:0;top:3830px" width="1200" height="353" role="img" aria-label="Photo of a lakeside mountain village fading into white">
    <defs><linearGradient id="conG" x1="0" y1="0" x2="0" y2="1">
      <stop offset="0" stop-color="#ffffff"/><stop offset=".35" stop-color="#b9c7a0"/>
      <stop offset=".7" stop-color="#6e8a5a"/><stop offset="1" stop-color="#8fa2a4"/></linearGradient></defs>
    <rect width="1200" height="353" fill="url(#conG)"/>
  </svg>
  <h2 class="heading" style="left:409px;top:3680px;font-size:57px">Contact Us</h2>
  <div class="field" style="left:234px;top:3784px;width:358px">First Name</div>
  <div class="field" style="left:605px;top:3784px;width:359px">Last Name</div>
  <div class="field" style="left:234px;top:3849px;width:358px">Email address</div>
  <div class="field" style="left:605px;top:3849px;width:359px">Phone Number</div>
  <div class="field" style="left:234px;top:3913px;width:730px;height:114px">Message</div>
  <a class="btn" style="left:541px;top:4059px;width:117px;height:41px;font-weight:400">Submit</a>
</section>

<footer class="site-footer">
  <a class="foot-link" style="left:153px">HOME</a>
  <a class="foot-link" style="left:229px">ABOUT</a>
  <a class="foot-link" style="left:309px">REVIEWS</a>
  <a class="foot-link" style="left:404px">CONTACT US</a>
  <a class="foot-link" style="left:523px">BOOKING</a>
  <p class="abs" style="left:153px;top:74px;font-size:12px">© 2022 Cedar Lantern. All rights reserved.Privacy &nbsp;|&nbsp; Terms of Use</p>
  <span class="social" style="left:151px;top:113px"></span>
  <span class="social" style="left:201px;top:113px"></span>
  <span class="social" style="left:250px;top:113px"></span>
  <span class="social" style="left:297px;top:113px"></span>
  <h3 class="abs" style="left:696px;top:40px;font-size:21px;font-weight:700">SIGN UP NEWSLETTER</h3>
  <div class="abs" style="left:696px;top:88px;width:351px;height:41px;background:var(--white);border-radius:21px;color:#444;font-size:12px;padding:13px 0 0 33px">Enter Email</div>
  <a class="btn" style="left:928px;top:88px;width:119px;height:41px;font-weight:400">Sign Up</a>
</footer>

</body>
</html>
```